Document Proposal to be designed with Graphics and Professional looking

This is a letter to be sent to generate interest as a proposal for a Pharmaceutical Sale. The figure in the document are from different articles explaining the systems I will attach pictures. I am not sure if I want to use my official Logo, please feel free to place something appropriate for illustration purposes only

```html
<!DOCTYPE html>
<html lang="en">
<head>
<meta charset="utf-8">
<title>Pharmaceutical Distribution Proposal</title>
<link href="https://fonts.googleapis.com/css2?family=Lato:wght@400;700;900&family=Oswald:wght@500&display=swap" rel="stylesheet">
<style>
:root{
  --blue:#3559c7;
  --navy:#1f3a7a;
  --cyan:#1eaee8;
  --red:#e3232c;
  --green:#7cc242;
  --ink:#2a2a2a;
  --muted:#8a8f99;
  --line:#c9d6ee;
  --paper:#ffffff;
  --bg:#ffffff;
}
*{box-sizing:border-box;margin:0;padding:0}
html,body{width:1200px;height:3223px;overflow:hidden;background:var(--bg)}
body{position:relative;font-family:"Lato",sans-serif;color:var(--ink)}
.page{position:absolute;width:382px;height:492px;background:var(--paper);box-shadow:2px 3px 6px rgba(0,0,0,.28);overflow:hidden}
.page .frame{position:absolute;inset:0;width:100%;height:100%}
.col-a{left:209px}.col-b{left:622px}
.row-1{top:89px}.row-2{top:600px}.row-3{top:1111px}.row-4{top:1623px}.row-5{top:2132px}.row-6{top:2640px}
.body{position:absolute;left:24px;right:24px;font-size:5.3px;line-height:1.38;text-align:justify}
.body p{margin-bottom:5px}
.body b{font-weight:700}
.hl{color:var(--blue)}
.logo-mark{position:absolute;left:268px;top:20px;width:98px;height:98px;border-radius:50%;background:#f1f2f4;display:flex;align-items:center;justify-content:center;font-size:6px;color:var(--blue);font-weight:700}
.badge{position:absolute;right:16px;top:14px;background:var(--red);color:#fff;font-family:"Oswald",sans-serif;font-weight:500;font-size:10px;padding:3px 12px;border-radius:10px;letter-spacing:.2px}
.pill-gray{position:absolute;left:132px;top:72px;background:#d4d6da;color:var(--blue);font-family:"Oswald",sans-serif;font-size:9.5px;padding:4px 18px;border-radius:10px}
.fig-box{position:absolute;border:1.5px solid #8fb8e8;background:#fff}
.fig-head{background:var(--cyan);color:#fff;font-weight:900;font-size:6px;text-align:center;padding:3px 4px;letter-spacing:.3px}
.placeholder{position:absolute}
.gmp-box{position:absolute;left:24px;top:152px;width:172px;height:184px;background:var(--cyan);color:#fff;font-size:5.3px;font-weight:700;line-height:1.4;padding:20px 14px;text-align:justify}
.col-text{position:absolute;left:210px;right:24px;font-size:5.3px;line-height:1.38;text-align:justify}
.col-text p{margin-bottom:5px}
.lims-table{position:absolute;left:22px;right:22px;font-size:4.4px;border-collapse:collapse;width:338px}
.lims-table th{background:var(--navy);color:#fff;text-align:left;padding:2px 3px;font-weight:700}
.lims-table td{padding:2px 3px;color:#fff;font-weight:700;border-bottom:1px solid #fff}
.lims-table td:first-child{background:var(--blue);width:100px}
.lims-table td:last-child{background:var(--green)}
.caption{position:absolute;font-size:4.6px;color:var(--blue)}
.tbl{position:absolute;left:18px;right:18px;border:1px solid var(--line);padding:4px 5px}
.th,.tr{display:grid;grid-template-columns:32px 12px 78px 18px 10px 60px 26px 22px 16px 20px;gap:3px;align-items:center}
.th{font-size:3.4px;font-weight:700;color:#555;border-bottom:1px solid var(--line);padding-bottom:2px}
.tr{font-size:3.3px;color:var(--blue);border-bottom:1px solid #e8eef8;padding:3px 0;line-height:1.3}
.tr .thumb{width:12px;height:10px;background:#c7d3e6}
.tr .desc b{color:#333}
.tr .dots{display:flex;gap:1.5px;flex-wrap:wrap}
.tr .dots i{width:3px;height:3px;border-radius:50%;background:var(--green);display:block}
.tr .uoi,.tr .price{color:#444}
.tr .qty{width:14px;height:6px;border:1px solid #ccc}
.tr .add{background:var(--cyan);color:#fff;text-align:center;font-weight:700;padding:1px 0;border-radius:1px}
.tr .fav{color:var(--muted)}
.sub-label{font-size:4.4px;color:var(--ink);margin:6px 0 3px}
.pd{position:absolute;left:18px;right:18px;border:1px solid var(--line)}
.pd-head{background:var(--cyan);color:#fff;text-align:center;font-weight:900;font-size:6.5px;letter-spacing:2px;padding:3px}
.pd-main{display:flex;gap:10px;padding:8px}
.pd-img{width:110px;height:76px;background:linear-gradient(#e2e4e6,#c9ccd0)}
.pd-noimg{width:110px;height:76px;background:#1d6fb3;color:#fff;display:flex;flex-direction:column;align-items:center;justify-content:center;font-weight:900;font-size:9px;line-height:1.05}
.pd-noimg .ic{width:22px;height:22px;border:2px solid #fff;border-radius:50%;margin-bottom:4px}
.pd-title{font-size:8px;color:var(--blue);margin-bottom:4px}
.pd-meta{font-size:4.2px;line-height:1.5;color:#333}
.pd-add{display:flex;gap:4px;margin-top:6px}
.pd-add span{font-size:4px;border:1px solid #ccc;padding:1px 6px}
.pd-add span.btn{background:var(--cyan);color:#fff;border-color:var(--cyan);font-weight:700}
.pd-grid{display:grid;grid-template-columns:48px 92px 48px 1fr;font-size:3.6px;line-height:1.6;padding:4px 8px 8px;color:#333}
.pd-grid b{font-weight:700}
.page-title{position:absolute;left:0;right:0;text-align:center;font-size:5.5px;font-weight:700}
</style>
</head>
<body>

<svg width="0" height="0" style="position:absolute" aria-hidden="true">
  <defs>
    <symbol id="page-frame" viewBox="0 0 382 492" preserveAspectRatio="none">
      <path d="M0 0H215C140 8 60 26 0 58Z" fill="#3559c7"/>
      <path d="M0 58C60 26 140 8 215 0H240C150 12 70 32 0 70Z" fill="#1eaee8"/>
      <path d="M0 418C120 452 270 440 382 396V492H0Z" fill="#3559c7"/>
      <path d="M0 436C130 468 280 452 382 404V414C280 466 120 478 0 452Z" fill="#1eaee8"/>
      <path d="M0 450C130 482 290 466 382 414V428C290 480 120 492 0 470Z" fill="#e3232c"/>
    </symbol>
  </defs>
</svg>

<!-- Page 1: cover letter -->
<section class="page col-a row-1">
  <svg class="frame"><use href="#page-frame"/></svg>
  <div class="logo-mark">LOGO</div>
  <div class="body" style="top:136px">
    <p><b>Dear Reader,</b></p>
    <p><b>Thank you for the opportunity to present our services and products.<br>Please review some information about our process and distribution, as well as some examples of products we can provide you with.</b></p>
    <p>We work with NDAB Accredited Drug Distributors to ensure strict standards and compliance processes; this ensures that licensure verifications, operational policies, and procedures, as well as proper and approved Drugs, are distributed. The Accreditation was put in place to ensure end buyers, which are Pharmacies that the drugs purchased are not counterfeit and are coming from the Brands and Manufacturers directly.</p>
    <p>In short, the NDAB Accreditation is important because it ensures the drugs you are paying for are genuine articles. With the rise of counterfeit drugs and wholesale distributors, NDAB created these rules to combat illegitimate wholesalers. That's also why we offer pedigree tracing for our drugs so you can rest assured the drugs you order are the ones your receive.</p>
    <p>We have access to most, if not all, FDA Brand name and Generic Equivalent medications. To give you some examples, please see some of the top medications which are currently distributed in United States Pharmacies, we have included them at the end of this document as Attachment A.</p>
    <p><b>Please provide us with a list of medications and quantities of the medication you are looking for; we will then reach out to our multiple warehouse distributors to find the best possible distributor to offer you as a possible option.</b></p>
  </div>
  <div class="body" style="top:368px">COMPANY INFORMATION</div>
</section>

<!-- Page 2: buy and bill -->
<section class="page col-b row-1">
  <svg class="frame"><use href="#page-frame"/></svg>
  <div class="badge">BUY &amp; BILL SYSTEM</div>
  <div class="body" style="top:42px;left:100px;text-align:right">Our Clinic uses what is referred to in the industry as a <b class="hl">BUY AND BILL SYSTEM</b>.<br>In this flowchart below, we are the CLINIC = us; we work with multiple Rx Wholesalers,<br>and in return, Rx Wholesalers work directly with Brands Manufacturers.</div>
  <div class="fig-box" style="left:22px;top:72px;width:338px;height:148px">
    <div class="fig-head">DISTRIBUTION &amp; REIMBURSEMENT OF PROVIDER-ADMINISTERED OUTPATIENT DRUGS:<br>BUY AND BILL</div>
    <div role="img" aria-label="Buy and bill flowchart showing product, payment and contract flows between manufacturer, wholesaler, clinic, payer and patient" style="margin:6px;height:122px;background:linear-gradient(135deg,#f4f6fb,#dfe7f5 50%,#f7f0f0)"></div>
  </div>
  <div class="body" style="top:232px">
    <p>Track and Trace is a method of following a product through the supply chain. In the pharmaceutical industry, this is often referred to as an e-pedigree. Government mandates to serialize pharmaceutical products are increasing around the globe. E-pedigree or electronic pedigree is an electronic version of the drug pedigree document. As defined by the U.S Food and Drug Administration as part of the 2006 Compliance Policy Guide for the Prescription Drug Marketing Act - "A drug pedigree is a statement of origin that identifies each prior sale, purchase, or trade of a drug, including the date of those transactions and the names and addresses of all parties to them."</p>
    <p><span class="hl">As a product moves from one place to the next, each company that handles the product must carry forward all of the previous e-pedigree information.</span> When it reaches it's final destination, the retailer will have a complete document showing where that shipment has been and who has handled that shipment. This is done for many reasons. The primary reason is for safety. It helps protect consumers from contaminated medicine and counterfeit drugs. It also has benefits to the manufacturer. Having the ability to serialize down to the unit level can help cut costs associated with recalls, as well as being able to more efficiently manage their shipments.</p>
    <p><span class="hl">The first critical piece of the chain occurs right on the packaging line.</span> Precise and consistent product handling, marking, inspection and data gathering are required to introduce accurate data into the front end of the system. Although pressure-sensitive labeling is the most common form of marking for bundles, cases and pallets, laser marking and ink jet coding are more common for units, because of space limitations and throughput speed requirements.</p>
  </div>
</section>

<!-- Page 3: manufacturing and GMP -->
<section class="page col-a row-2">
  <svg class="frame"><use href="#page-frame"/></svg>
  <div class="body" style="top:52px">
    <p>All manufacturing flows, whether making cars, pies, medical devices, or pharmaceuticals, take raw materials, and through a series of manufacturing processes, transform them into a final product. In pharmaceutical production the constituent parts include the active pharmaceutical ingredient (API), excipients, and packaging and labelling materials.</p>
    <p>Pharmaceuticals in tablet form may have coating agents added to make them easier to swallow and coloring to differentiate them. Tablets are often packaged in blister packs of 20 or so with a cardboard carton on which key consumer information is printed. As with cars or ice cream each constituent part from the API to the foil of the blister pack must be traceable back to the originating batch of each originating supplier. If multiple batches of the same material are used this must become part of the production record. The key is traceability; traceability of everything that went into the batch of a product.</p>
  </div>
  <div class="gmp-box">The GMP principles put forward by the US Food and Drug Administration help ensure the quality of manufactured products throughout the manufacturing, processing and packaging stages. They are used to create a quality framework for the manufacture of a wide variety of products, including drugs, medical devices, some food, and blood, to make sure that the products are safe, pure and effective. GMP principles address a wide range of issues as varied as recordkeeping, personnel qualifications, sanitation, cleanliness, equipment verification, process validation, and complaint handling, but offer individual manufacturers the flexibility to decide how to implement the necessary controls in the most appropriate way for their particular business.</div>
  <div class="col-text" style="top:156px">
    <p>Per US FDA, Good Manufacturing Practice (cGMP) and FDA 21 CFR Part 11 in pharmaceutical companies is a key regulatory requirements.</p>
    <p>To meet these GMP requirements is extremely important. The failure of organizations to comply with GMP regulations in any context can result in very serious consequences. These include internal direct costs related to product failure, scrap, etc and remediation costs related to problem identification, correction and reporting.</p>
    <p>There could also be significant external costs such as regulatory action costs related to recalls, discontinuation, suspended operations, etc. There may be costs associated with loss of market share due to reduced product volume. There is also the cost associated with damage to the company's reputation, which can even affect share value.</p>
  </div>
  <div class="placeholder" role="img" aria-label="Photo of assorted colourful tablets and capsules" style="left:0;top:348px;width:230px;height:72px;background:linear-gradient(90deg,#e9d9cf,#c94b4b 40%,#f1efe9 70%,#fff)"></div>
</section>

<!-- Page 4: production line -->
<section class="page col-b row-2">
  <svg class="frame"><use href="#page-frame"/></svg>
  <div class="fig-box" style="left:96px;top:22px;width:266px;height:176px">
    <div class="fig-head">FIGURE 1: TYPICAL PHARMACEUTICAL TABLET PRODUCTION LINE</div>
    <div role="img" aria-label="Diagram of tablet production equipment from API and excipients through mill, granulator, dryer, tablet press and packaging" style="margin:6px;height:146px;background:linear-gradient(135deg,#e4ecfa,#b9cbee 60%,#e9eef7)"></div>
  </div>
  <div class="body" style="top:210px">
    <p>An overview of a typical pharmaceutical tablet production line is shown in Figure 1. Like cooking, the exact proportions of the various raw ingredients are controlled by a recipe which defines the amount of API, and excipient required. The various ingredients may be milled and mixed to ensure an even distribution of API. Mixing can be performed as a slurry/wet mix which is dried and milled again to create a fine powder. This bulk powder may be mixed with further excipients before being formed into tablets in a tableting machine. The tablets may be coated and finally packaged as required.</p>
    <p>Testing will be performed at each critical stage of the flow from raw materials to the final packaged product. For example, the incoming raw materials may be re-tested to ensure they conform to the supplier's specification before being released for use. The output of the granulator may be tested to ensure the API is evenly mixed and the output from the milling checked to ensure the mixture still contains the correct proportions of API and is ground evenly. Samples of tablet from the final product are retained for dissolution, stability, and other quality assurance purposes.</p>
    <p>All LIMS require the ability to track samples and associated test results, create certificates of analysis (CofA), use barcoding and associate samples with key information such as batch and supplier. LIMS will also include the ability to manage calibration and maintenance of laboratory instruments, and records which instruments were used for each sample test, along with who tested that sample and whether they were competent to test it, and to control inventory of the chemicals and the laboratory consumables used in testing.</p>
    <p>But while a typical QC sampling flow monitors and reports on discreet samples, a manufacturing flow requires a broader range of information to be associated and combined for management and reporting. A manufacturing flow requires the addition of Recipe Management to control the raw materials and intermediate products going into each manufacturing batch; the ability to keep test results for each part of the flow (raw materials, intermediate stages and final product); to link test results to the originating raw materials/suppliers and final product/customers; the statistical tools to control the process within defined limits; and the ability to quickly retrieve and report on this data.</p>
  </div>
</section>

<!-- Page 5: LIMS workflow -->
<section class="page col-a row-3">
  <svg class="frame"><use href="#page-frame"/></svg>
  <div class="body" style="top:16px;left:150px;font-size:5.2px">Laboratory information management systems (LIMS) are used extensively in laboratories in a huge number of industries to manage, track and report on samples, tests, test results and more. In manufacturing industries laboratory testing can be involved at every step, from raw material analysis through to the finished product</div>
  <div class="fig-box" style="left:20px;top:62px;width:342px;height:252px">
    <div class="fig-head">LUMEO LABS LIMS WORKFLOW</div>
    <div role="img" aria-label="Circular LIMS workflow diagram: sample reception, batching, preparation, analysis request, results capture, quality control, verification and publication" style="margin:8px 24px;height:222px;border-radius:50%;background:radial-gradient(circle,#ffffff 30%,#dbe6f6 55%,#f4f7fb 75%)"></div>
  </div>
  <div class="placeholder" role="img" aria-label="Photo of a laboratory scientist handling sample vials" style="left:40px;top:322px;width:300px;height:96px;background:linear-gradient(90deg,#dfe6ec,#f4f4f2 40%,#9fc3e6 60%,#eef1f4)"></div>
</section>

<!-- Page 6: key elements -->
<section class="page col-b row-3">
  <svg class="frame"><use href="#page-frame"/></svg>
  <div class="badge" style="top:32px">KEY ELEMENTS OF A MANUFACTURING LIMS</div>
  <div class="caption" style="left:26px;top:68px">Key elements specific to the pharmaceutical manufacturing LIMS include:</div>
  <table class="lims-table" style="top:88px">
    <tr><th>Element</th><th>Description</th></tr>
    <tr><td>Materials Management</td><td>Defines raw, intermediate and final products (RM, IP and FP) used or manufactured</td></tr>
    <tr><td>Supplier Management</td><td>Manages suppliers and defines the raw materials they supply</td></tr>
    <tr><td>Recipe Management</td><td>Identifies the component materials that go into the products</td></tr>
    <tr><td>Batch Management</td><td>Defines the steps that batch manufacture is handled in the LIMS</td></tr>
    <tr><td>Batch Genealogy</td><td>Controls the ability to track and trace component materials for a product</td></tr>
    <tr><td>Test Management</td><td>Defines the testing that the batches will undergo</td></tr>
    <tr><td>Specification Management</td><td>Describes the manufacturing specifications the batches must be tested against</td></tr>
  </table>
  <div class="caption" style="left:26px;top:196px">Other key elements include:</div>
  <table class="lims-table" style="top:208px">
    <tr><th>Element</th><th>Description</th></tr>
    <tr><td>ICMS Management</td><td>Instrument calibration and maintenance management and tracking</td></tr>
    <tr><td>Competency Management</td><td>Tracking and management of analyst training and certification</td></tr>
    <tr><td>CAPA Management</td><td>Corrective and Preventive actions for the quality cycle</td></tr>
    <tr><td>Product Grading</td><td>Allows the grading of a product against alternative and possibly multiple specifications</td></tr>
    <tr><td>Frequency Testing</td><td>Implement reduced testing regimes based on previous results to experience, especially useful for raw materials and trusted suppliers</td></tr>
    <tr><td>Environmental Monitoring</td><td>Monitor the production environment to ensure cleanliness</td></tr>
    <tr><td>Stability Management</td><td>Manages the storage and shelf life/QA testing of product samples</td></tr>
  </table>
  <div class="placeholder" role="img" aria-label="Illustration of interlocking gears with laboratory and industry icons" style="left:66px;top:328px;width:250px;height:74px;background:radial-gradient(ellipse,#3a78c9,#1f4b8e 50%,#ffffff 72%)"></div>
</section>

<!-- Page 7: Attachment A -->
<section class="page col-a row-4">
  <svg class="frame"><use href="#page-frame"/></svg>
  <div class="pill-gray">ATTACHMENT A</div>
  <div class="body" style="top:106px;left:22px;right:22px;font-size:5px"><b>Figure 1</b> shows the Top 11 Brand Prescription Medications currently being distributed in the United States. The pricing is placed as an example, and the final pricing is always negotiated with the warehouse before the order is placed due to factors such as quantity, current capacity, and the size of the full order.</div>
  <div class="tbl" style="top:140px;height:210px">
    <div class="th"><span>ITEM# / NDC</span><span></span><span>DESCRIPTION / MFG</span><span>ATTR.</span><span>UOI</span><span>GPI DESCRIPTION</span><span>ITEM PRICE</span><span>QTY</span><span></span><span>ACTION</span></div>
    <div class="tr"><span>2004981<br>70010014001</span><span class="thumb" role="img" aria-label="product photo"></span><span class="desc">ACETAVEL ER TB 650MG GRAN 100<br><b>MFG:</b> CORVANE PHARMA INC</span><span class="dots"><i></i><i></i></span><span class="uoi">EA</span><span>ACETAVEL TAB ER 650 MG</span><span class="price">$5.41</span><span class="qty"></span><span class="add">ADD</span><span class="fav">♡ Fav</span></div>
    <div class="tr"><span>1088420<br>00173069600</span><span class="thumb" role="img" aria-label="product photo"></span><span class="desc">FLUTICASONE SALMETEROL INH 250<br><b>MFG:</b> NORBEL PHARMA LLC</span><span class="dots"><i></i><i></i></span><span class="uoi">EA</span><span>FLUTICASONE SALMETEROL INH</span><span class="price">$384.17</span><span class="qty"></span><span class="add">ADD</span><span class="fav">♡ Fav</span></div>
    <div class="tr"><span>2274624<br>00006027731</span><span class="thumb" role="img" aria-label="product photo"></span><span class="desc">SITAGLIPTIN TB 100MG 90<br><b>MFG:</b> NORBEL PHARMA LLC</span><span class="dots"><i></i><i></i></span><span class="uoi">EA</span><span>SITAGLIPTIN TAB 100 MG</span><span class="price">$1,528.70</span><span class="qty"></span><span class="add">ADD</span><span class="fav">♡ Fav</span></div>
    <div class="tr"><span>1065009<br>00169413812</span><span class="thumb" role="img" aria-label="product photo"></span><span class="desc">INSULIN ASPART PEN 3ML 5<br><b>MFG:</b> HALDEN BIO INC</span><span class="dots"><i></i><i></i></span><span class="uoi">EA</span><span>INSULIN ASPART INJ PEN</span><span class="price">$559.80</span><span class="qty"></span><span class="add">ADD</span><span class="fav">♡ Fav</span></div>
    <div class="tr"><span>2223985<br>00597014030</span><span class="thumb" role="img" aria-label="product photo"></span><span class="desc">LINAGLIPTIN TB 5MG 30<br><b>MFG:</b> ORVEN PHARMA CO</span><span class="dots"><i></i><i></i></span><span class="uoi">EA</span><span>LINAGLIPTIN TAB 5 MG</span><span class="price">$482.24</span><span class="qty"></span><span class="add">ADD</span><span class="fav">♡ Fav</span></div>
    <div class="tr"><span>2151079<br>00310620530</span><span class="thumb" role="img" aria-label="product photo"></span><span class="desc">DAPAGLIFLOZIN TB 10MG 30<br><b>MFG:</b> ALDER THERAPEUTICS</span><span class="dots"><i></i><i></i></span><span class="uoi">EA</span><span>DAPAGLIFLOZIN TAB 10 MG</span><span class="price">$517.60</span><span class="qty"></span><span class="add">ADD</span><span class="fav">♡ Fav</span></div>
    <div class="tr"><span>2260136<br>50458057830</span><span class="thumb" role="img" aria-label="product photo"></span><span class="desc">RIVAROXABAN TB 20MG 30<br><b>MFG:</b> HALDEN BIO INC</span><span class="dots"><i></i><i></i></span><span class="uoi">EA</span><span>RIVAROXABAN TAB 20 MG</span><span class="price">$497.19</span><span class="qty"></span><span class="add">ADD</span><span class="fav">♡ Fav</span></div>
    <div class="tr"><span>2087552<br>00003089321</span><span class="thumb" role="img" aria-label="product photo"></span><span class="desc">APIXABAN TB 5MG 60<br><b>MFG:</b> ALDER THERAPEUTICS</span><span class="dots"><i></i><i></i></span><span class="uoi">EA</span><span>APIXABAN TAB 5 MG</span><span class="price">$529.40</span><span class="qty"></span><span class="add">ADD</span><span class="fav">♡ Fav</span></div>
    <div class="tr"><span>2211843<br>00002143380</span><span class="thumb" role="img" aria-label="product photo"></span><span class="desc">DULAGLUTIDE PEN 1.5MG 4<br><b>MFG:</b> ORVEN PHARMA CO</span><span class="dots"><i></i><i></i></span><span class="uoi">EA</span><span>DULAGLUTIDE INJ PEN 1.5 MG</span><span class="price">$857.21</span><span class="qty"></span><span class="add">ADD</span><span class="fav">♡ Fav</span></div>
    <div class="tr"><span>2290117<br>00173088210</span><span class="thumb" role="img" aria-label="product photo"></span><span class="desc">ALBUTEROL INH 90MCG 1<br><b>MFG:</b> NORBEL PHARMA LLC</span><span class="dots"><i></i><i></i></span><span class="uoi">EA</span><span>ALBUTEROL INH AER 90 MCG</span><span class="price">$62.88</span><span class="qty"></span><span class="add">ADD</span><span class="fav">♡ Fav</span></div>
    <div class="tr"><span>2187304<br>00078065961</span><span class="thumb" role="img" aria-label="product photo"></span><span class="desc">SACUBITRIL VALSARTAN TB 60<br><b>MFG:</b> KESTRA PHARMA</span><span class="dots"><i></i><i></i></span><span class="uoi">EA</span><span>SACUBITRIL VALSARTAN TAB</span><span class="price">$595.30</span><span class="qty"></span><span class="add">ADD</span><span class="fav">♡ Fav</span></div>
  </div>
</section>

<!-- Page 8: Figure 2 product detail -->
<section class="page col-b row-4">
  <svg class="frame"><use href="#page-frame"/></svg>
  <div class="body" style="top:72px;left:22px;right:22px;font-size:5px"><b>Figure 2</b>. If the preference is for Generic Equivalent, we can also provide options for your consideration and review. Figure 3, shows some options for the Figure 2 product, Acetavel. (Please note these images are presented as samples, but the actual information will be exactly as shown)</div>
  <div class="pd" style="top:108px">
    <div class="pd-head">PRODUCT DETAIL</div>
    <div class="pd-main">
      <div class="pd-img" role="img" aria-label="Photo of a white oblong tablet"></div>
      <div>
        <div class="pd-title">ACETAVEL ER TB 650MG GRAN 100</div>
        <div class="pd-meta">PRODUCT#: 2004981<br>NDC#: 70010014001<br>CASE QTY: 36.0</div>
        <div class="pd-add"><span>1</span><span class="btn">ADD</span></div>
      </div>
    </div>
    <div class="pd-grid">
      <b>Item Description :</b><span>ACETAVEL ER TB 650MG GRAN 100</span><b>Manufacturer :</b><span>CORVANE PHARMACEUTICALS INC</span>
      <b>ItemNumber :</b><span>2004981</span><b>Product Size :</b><span>100</span>
      <b>NDC :</b><span>70010014001</span><b>Case Quantity :</b><span>36</span>
      <b>UOM :</b><span>EA</span><b>Price :</b><span>$5.41</span>
      <b>OBR :</b><span>MR</span><b>WAC :</b><span>$7.47</span>
      <b>Strength :</b><span>650 MG</span><b>AWP :</b><span>$8.34</span>
      <b>Country Of Origin :</b><span>US</span><b>GPI Description :</b><span>Acetavel Tab ER 650 MG</span>
    </div>
  </div>
</section>

<!-- Page 9: Figure 3 generics -->
<section class="page col-a row-5">
  <svg class="frame"><use href="#page-frame"/></svg>
  <div class="page-title" style="top:76px">Figure 3</div>
  <div class="tbl" style="top:88px;border:none;padding:0 5px">
    <div class="th"><span>ITEM# / NDC</span><span></span><span>DESCRIPTION / MFG</span><span>ATTR.</span><span>UOI</span><span>GPI DESCRIPTION</span><span>ITEM PRICE</span><span>QTY</span><span></span><span>ACTION</span></div>
    <div class="tr"><span>2004981<br>70010014001</span><span class="thumb" role="img" aria-label="product photo"></span><span class="desc">ACETAVEL ER TB 650MG GRAN 100<br><b>MFG:</b> CORVANE PHARMA INC</span><span class="dots"><i></i><i></i></span><span class="uoi">EA</span><span>ACETAVEL TAB ER 650 MG</span><span class="price">$5.41</span><span class="qty"></span><span class="add">ADD</span><span class="fav">♡ Fav</span></div>
    <div class="sub-label">Generic Equivalents</div>
    <div class="th"><span>ITEM# / NDC</span><span></span><span>DESCRIPTION / MFG</span><span>ATTR.</span><span>UOI</span><span>GPI DESCRIPTION</span><span>ITEM PRICE</span><span>QTY</span><span></span><span>ACTION</span></div>
    <div class="tr"><span>3531928<br>50268005215</span><span class="thumb" role="img" aria-label="product photo"></span><span class="desc">ACETAVEL ER TAB 650MG AVKD50<br><b>MFG:</b> MERIDEL LLC</span><span class="dots"><i></i><i></i></span><span class="uoi">EA</span><span>ACETAVEL TAB ER 650 MG</span><span class="price">$2.78</span><span class="qty"></span><span class="add">ADD</span><span class="fav">♡ Fav</span></div>
    <div class="tr"><span>2068116<br>74880014601</span><span class="thumb" role="img" aria-label="product photo"></span><span class="desc">ACETAVEL ER TAB 650MG 100<br><b>MFG:</b> LINDEN PHARMA CO</span><span class="dots"><i></i><i></i></span><span class="uoi">EA</span><span>ACETAVEL TAB ER 650 MG</span><span class="price">$6.08</span><span class="qty"></span><span class="add">ADD</span><span class="fav">♡ Fav</span></div>
  </div>
  <div class="pd" style="top:190px">
    <div class="pd-head">PRODUCT DETAIL</div>
    <div class="pd-main">
      <div class="pd-noimg"><span class="ic"></span>No Image<br>Available</div>
      <div>
        <div class="pd-title">ACETAVEL ER TAB 650MG AVKD50</div>
        <div class="pd-meta">PRODUCT#: 3531928<br>NDC#: 50268005215<br>CASE QTY: 16.0</div>
      </div>
    </div>
    <div class="pd-grid">
      <b>Item Description :</b><span>ACETAVEL ER TAB 650MG AVKD50</span><b>Manufacturer :</b><span>MERIDEL LLC</span>
      <b>ItemNumber :</b><span>3531928</span><b>Product Size :</b><span>50</span>
      <b>NDC :</b><span>50268005215</span><b>Case Quantity :</b><span>16</span>
      <b>UOM :</b><span>EA</span><b>Price :</b><span>$2.78</span>
      <b>OBR :</b><span>MR</span><b>WAC :</b><span>$3.73</span>
      <b>Strength :</b><span>650 MG</span><b>AWP :</b><span>$4.21</span>
      <b>Country Of Origin :</b><span>US</span><b>GPI Description :</b><span>Acetavel Tab ER 650 MG</span>
    </div>
  </div>
</section>

<!-- Page 10: more examples -->
<section class="page col-b row-5">
  <svg class="frame"><use href="#page-frame"/></svg>
  <div class="page-title" style="top:40px">More Examples</div>
  <div class="tbl" style="top:54px;height:360px">
    <div class="th"><span>ITEM# / NDC</span><span></span><span>DESCRIPTION / MFG</span><span>ATTR.</span><span>UOI</span><span>GPI DESCRIPTION</span><span>ITEM PRICE</span><span>QTY</span><span></span><span>ACTION</span></div>
    <div class="tr"><span>1026330<br>51079096320</span><span class="thumb" role="img" aria-label="product photo"></span><span class="desc">ATORVASTATIN TB 40MG 90<br><b>MFG:</b> LINDEN PHARMA CO</span><span class="dots"><i></i><i></i></span><span class="uoi">EA</span><span>ATORVASTATIN TAB 40 MG</span><span class="price">$6.72</span><span class="qty"></span><span class="add">ADD</span><span class="fav">♡ Fav</span></div>
    <div class="tr"><span>1057311<br>68180051309</span><span class="thumb" role="img" aria-label="product photo"></span><span class="desc">LISINOPRIL TB 20MG 1000<br><b>MFG:</b> KESTRA PHARMA</span><span class="dots"><i></i><i></i></span><span class="uoi">EA</span><span>LISINOPRIL TAB 20 MG</span><span class="price">$23.50</span><span class="qty"></span><span class="add">ADD</span><span class="fav">♡ Fav</span></div>
    <div class="tr"><span>2113505<br>00093722098</span><span class="thumb" role="img" aria-label="product photo"></span><span class="desc">LEVOTHYROXINE TB 50MCG 90<br><b>MFG:</b> MERIDEL LLC</span><span class="dots"><i></i><i></i></span><span class="uoi">EA</span><span>LEVOTHYROXINE TAB 50 MCG</span><span class="price">$11.93</span><span class="qty"></span><span class="add">ADD</span><span class="fav">♡ Fav</span></div>
    <div class="tr"><span>1094526<br>65862000899</span><span class="thumb" role="img" aria-label="product photo"></span><span class="desc">METFORMIN TB 500MG 1000<br><b>MFG:</b> CORVANE PHARMA INC</span><span class="dots"><i></i><i></i></span><span class="uoi">EA</span><span>METFORMIN TAB 500 MG</span><span class="price">$14.80</span><span class="qty"></span><span class="add">ADD</span><span class="fav">♡ Fav</span></div>
    <div class="tr"><span>1181232<br>00378181001</span><span class="thumb" role="img" aria-label="product photo"></span><span class="desc">AMLODIPINE TB 10MG 500<br><b>MFG:</b> LINDEN PHARMA CO</span><span class="dots"><i></i><i></i></span><span class="uoi">EA</span><span>AMLODIPINE TAB 10 MG</span><span class="price">$9.14</span><span class="qty"></span><span class="add">ADD</span><span class="fav">♡ Fav</span></div>
    <div class="tr"><span>1040118<br>16729000517</span><span class="thumb" role="img" aria-label="product photo"></span><span class="desc">OMEPRAZOLE CP 20MG 1000<br><b>MFG:</b> KESTRA PHARMA</span><span class="dots"><i></i><i></i></span><span class="uoi">EA</span><span>OMEPRAZOLE CAP DR 20 MG</span><span class="price">$31.66</span><span class="qty"></span><span class="add">ADD</span><span class="fav">♡ Fav</span></div>
    <div class="tr"><span>1213390<br>00904671361</span><span class="thumb" role="img" aria-label="product photo"></span><span class="desc">LOSARTAN TB 50MG 90<br><b>MFG:</b> MERIDEL LLC</span><span class="dots"><i></i><i></i></span><span class="uoi">EA</span><span>LOSARTAN TAB 50 MG</span><span class="price">$4.27</span><span class="qty"></span><span class="add">ADD</span><span class="fav">♡ Fav</span></div>
    <div class="tr"><span>1140027<br>31722070190</span><span class="thumb" role="img" aria-label="product photo"></span><span class="desc">GABAPENTIN CP 300MG 100<br><b>MFG:</b> CORVANE PHARMA INC</span><span class="dots"><i></i><i></i></span><span class="uoi">EA</span><span>GABAPENTIN CAP 300 MG</span><span class="price">$5.39</span><span class="qty"></span><span class="add">ADD</span><span class="fav">♡ Fav</span></div>
    <div class="tr"><span>1166804<br>60505257809</span><span class="thumb" role="img" aria-label="product photo"></span><span class="desc">SERTRALINE TB 50MG 500<br><b>MFG:</b> LINDEN PHARMA CO</span><span class="dots"><i></i><i></i></span><span class="uoi">EA</span><span>SERTRALINE TAB 50 MG</span><span class="price">$12.05</span><span class="qty"></span><span class="add">ADD</span><span class="fav">♡ Fav</span></div>
    <div class="tr"><span>1201755<br>00781507210</span><span class="thumb" role="img" aria-label="product photo"></span><span class="desc">SIMVASTATIN TB 20MG 1000<br><b>MFG:</b> KESTRA PHARMA</span><span class="dots"><i></i><i></i></span><span class="uoi">EA</span><span>SIMVASTATIN TAB 20 MG</span><span class="price">$18.44</span><span class="qty"></span><span class="add">ADD</span><span class="fav">♡ Fav</span></div>
    <div class="tr"><span>1077643<br>00591540510</span><span class="thumb" role="img" aria-label="product photo"></span><span class="desc">HYDROCHLOROTHIAZIDE TB 25MG<br><b>MFG:</b> MERIDEL LLC</span><span class="dots"><i></i><i></i></span><span class="uoi">EA</span><span>HCTZ TAB 25 MG</span><span class="price">$3.62</span><span class="qty"></span><span class="add">ADD</span><span class="fav">♡ Fav</span></div>
    <div class="th" style="margin-top:6px"><span>ITEM# / NDC</span><span></span><span>DESCRIPTION / MFG</span><span>ATTR.</span><span>UOI</span><span>GPI DESCRIPTION</span><span>ITEM PRICE</span><span>QTY</span><span></span><span>ACTION</span></div>
    <div class="tr"><span>2301146<br>59762331001</span><span class="thumb" role="img" aria-label="product photo"></span><span class="desc">MONTELUKAST TB 10MG 30<br><b>MFG:</b> CORVANE PHARMA INC</span><span class="dots"><i></i><i></i></span><span class="uoi">EA</span><span>MONTELUKAST TAB 10 MG</span><span class="price">$4.88</span><span class="qty"></span><span class="add">ADD</span><span class="fav">♡ Fav</span></div>
    <div class="tr"><span>2301147<br>59762331002</span><span class="thumb" role="img" aria-label="product photo"></span><span class="desc">MONTELUKAST TB 10MG 90<br><b>MFG:</b> CORVANE PHARMA INC</span><span class="dots"><i></i><i></i></span><span class="uoi">EA</span><span>MONTELUKAST TAB 10 MG</span><span class="price">$9.75</span><span class="qty"></span><span class="add">ADD</span><span class="fav">♡ Fav</span></div>
    <div class="tr"><span>2301148<br>59762331003</span><span class="thumb" role="img" aria-label="product photo"></span><span class="desc">MONTELUKAST TB 10MG 500<br><b>MFG:</b> CORVANE PHARMA INC</span><span class="dots"><i></i><i></i></span><span class="uoi">EA</span><span>MONTELUKAST TAB 10 MG</span><span class="price">$41.20</span><span class="qty"></span><span class="add">ADD</span><span class="fav">♡ Fav</span></div>
    <div class="tr"><span>2301149<br>59762331004</span><span class="thumb" role="img" aria-label="product photo"></span><span class="desc">MONTELUKAST CHEW 5MG 30<br><b>MFG:</b> CORVANE PHARMA INC</span><span class="dots"><i></i><i></i></span><span class="uoi">EA</span><span>MONTELUKAST CHEW TAB 5 MG</span><span class="price">$6.31</span><span class="qty"></span><span class="add">ADD</span><span class="fav">♡ Fav</span></div>
    <div class="tr"><span>2301150<br>59762331005</span><span class="thumb" role="img" aria-label="product photo"></span><span class="desc">MONTELUKAST CHEW 4MG 30<br><b>MFG:</b> CORVANE PHARMA INC</span><span class="dots"><i></i><i></i></span><span class="uoi">EA</span><span>MONTELUKAST CHEW TAB 4 MG</span><span class="price">$6.02</span><span class="qty"></span><span class="add">ADD</span><span class="fav">♡ Fav</span></div>
    <div class="tr"><span>2301151<br>59762331006</span><span class="thumb" role="img" aria-label="product photo"></span><span class="desc">MONTELUKAST GRAN 4MG 30<br><b>MFG:</b> CORVANE PHARMA INC</span><span class="dots"><i></i><i></i></span><span class="uoi">EA</span><span>MONTELUKAST GRAN 4 MG</span><span class="price">$22.15</span><span class="qty"></span><span class="add">ADD</span><span class="fav">♡ Fav</span></div>
  </div>
</section>

<!-- Page 11: more examples -->
<section class="page col-a row-6">
  <svg class="frame"><use href="#page-frame"/></svg>
  <div class="page-title" style="top:40px">More Examples</div>
  <div class="tbl" style="top:54px;height:360px">
    <div class="tr"><span>2045530<br>00093505698</span><span class="thumb" role="img" aria-label="product photo"></span><span class="desc">ROSUVASTATIN TB 10MG 90<br><b>MFG:</b> LINDEN PHARMA CO</span><span class="dots"><i></i><i></i></span><span class="uoi">EA</span><span>ROSUVASTATIN TAB 10 MG</span><span class="price">$7.90</span><span class="qty"></span><span class="add">ADD</span><span class="fav">♡ Fav</span></div>
    <div class="tr"><span>2045531<br>00093505701</span><span class="thumb" role="img" aria-label="product photo"></span><span class="desc">ROSUVASTATIN TB 20MG 90<br><b>MFG:</b> LINDEN PHARMA CO</span><span class="dots"><i></i><i></i></span><span class="uoi">EA</span><span>ROSUVASTATIN TAB 20 MG</span><span class="price">$8.45</span><span class="qty"></span><span class="add">ADD</span><span class="fav">♡ Fav</span></div>
    <div class="tr"><span>2078802<br>68382013610</span><span class="thumb" role="img" aria-label="product photo"></span><span class="desc">PANTOPRAZOLE TB 40MG 1000<br><b>MFG:</b> KESTRA PHARMA</span><span class="dots"><i></i><i></i></span><span class="uoi">EA</span><span>PANTOPRAZOLE TAB DR 40 MG</span><span class="price">$38.12</span><span class="qty"></span><span class="add">ADD</span><span class="fav">♡ Fav</span></div>
    <div class="tr"><span>2110394<br>00378018801</span><span class="thumb" role="img" aria-label="product photo"></span><span class="desc">TRAZODONE TB 50MG 100<br><b>MFG:</b> MERIDEL LLC</span><span class="dots"><i></i><i></i></span><span class="uoi">EA</span><span>TRAZODONE TAB 50 MG</span><span class="price">$3.18</span><span class="qty"></span><span class="add">ADD</span><span class="fav">♡ Fav</span></div>
    <div class="tr"><span>2110395<br>00378018810</span><span class="thumb" role="img" aria-label="product photo"></span><span class="desc">TRAZODONE TB 50MG 1000<br><b>MFG:</b> MERIDEL LLC</span><span class="dots"><i></i><i></i></span><span class="uoi">EA</span><span>TRAZODONE TAB 50 MG</span><span class="price">$22.47</span><span class="qty"></span><span class="add">ADD</span><span class="fav">♡ Fav</span></div>
    <div class="tr"><span>2134417<br>00591088401</span><span class="thumb" role="img" aria-label="product photo"></span><span class="desc">METOPROLOL TB 25MG 100<br><b>MFG:</b> CORVANE PHARMA INC</span><span class="dots"><i></i><i></i></span><span class="uoi">EA</span><span>METOPROLOL TAB 25 MG</span><span class="price">$2.96</span><span class="qty"></span><span class="add">ADD</span><span class="fav">♡ Fav</span></div>
    <div class="tr"><span>2134418<br>00591088410</span><span class="thumb" role="img" aria-label="product photo"></span><span class="desc">METOPROLOL TB 25MG 1000<br><b>MFG:</b> CORVANE PHARMA INC</span><span class="dots"><i></i><i></i></span><span class="uoi">EA</span><span>METOPROLOL TAB 25 MG</span><span class="price">$19.80</span><span class="qty"></span><span class="add">ADD</span><span class="fav">♡ Fav</span></div>
    <div class="tr"><span>2159022<br>16714010101</span><span class="thumb" role="img" aria-label="product photo"></span><span class="desc">ESCITALOPRAM TB 10MG 100<br><b>MFG:</b> LINDEN PHARMA CO</span><span class="dots"><i></i><i></i></span><span class="uoi">EA</span><span>ESCITALOPRAM TAB 10 MG</span><span class="price">$4.55</span><span class="qty"></span><span class="add">ADD</span><span class="fav">♡ Fav</span></div>
  </div>
</section>

</body>
</html>
```